Halvercott Orthodontics business card

Using our existing logo (created with ArtFolio), please create a tasteful, contemporary business card. We are father and daughter orthodontists specializing in braces, clarafit, etc to design healthy, beautiful smiles for children, adolescents, and adults. We would like the design to be family-friendly but not childish.
The final design should include all of the information without looking cluttered (I hope! If necessary to achieve an optimal design, please consider making the card double-sided)
Purple, black, silver on a white card
Please include the following information:
Halvercott Orthodontics (logo)
Marguerite L. Halvercott, DMD
Douglas R. Halvercott, DMD

312 Bramblewood Street
North Andover, MA 01899
978.555.0142

847C Quarry Hollow Street
Methuen, MA 01898
978.555.0187

email frontdesk@halvercottortho.example
website www.halvercottortho.example

```html
<!DOCTYPE html>
<html lang="en">
<head>
<meta charset="utf-8">
<title>Halvercott Orthodontics business card</title>
<link href="https://fonts.googleapis.com/css2?family=Open+Sans:wght@400;600;700&display=swap" rel="stylesheet">
<style>
  :root {
    --purple: #652d90;
    --white: #ffffff;
    --grey: #6d6e71;
    --silver: #a7a9ac;
    --rule: #d9d9d9;
    --backdrop: #2b2c2f;
    --backdrop-dark: #141517;
  }
  * { margin: 0; padding: 0; box-sizing: border-box; }
  html, body { width: 1200px; height: 952px; overflow: hidden; }
  body {
    background: radial-gradient(ellipse at 55% 50%, var(--backdrop) 0%, var(--backdrop-dark) 80%);
    font-family: "Open Sans", sans-serif;
    position: relative;
  }
  .card {
    position: absolute;
    width: 560px;
    height: 320px;
    box-shadow: 0 18px 40px rgba(0,0,0,.55);
  }
  /* Back side */
  .card-back {
    left: 580px; top: 120px;
    background: var(--purple);
    display: flex; align-items: center; justify-content: center;
  }
  .wordmark { display: flex; align-items: center; gap: 16px; }
  .wordmark-dot {
    width: 46px; height: 46px; border-radius: 50%;
    border: 3px solid currentColor;
  }
  .wordmark-text { font-weight: 600; line-height: 1; }
  .wordmark-name { display: block; font-size: 34px; letter-spacing: 1px; }
  .wordmark-sub { display: block; font-size: 13px; letter-spacing: 7px; margin-top: 6px; }
  .card-back .wordmark { color: var(--white); }

  /* Front side */
  .card-front {
    left: 60px; top: 500px;
    background: var(--white);
  }
  .accent-bar { position: absolute; width: 12px; background: var(--purple); }
  .accent-bar.left { left: 0; top: 26px; height: 130px; }
  .accent-bar.right { right: 0; bottom: 26px; height: 130px; }
  .card-front .wordmark {
    position: absolute; left: 40px; top: 56px; color: var(--purple); gap: 10px;
  }
  .card-front .wordmark-dot { width: 30px; height: 30px; border-width: 2px; }
  .card-front .wordmark-name { font-size: 23px; }
  .card-front .wordmark-sub { font-size: 9px; letter-spacing: 4.6px; margin-top: 5px; }
  .divider {
    position: absolute; left: 262px; top: 34px; width: 1px; height: 140px;
    background: var(--rule);
  }
  .contact { position: absolute; left: 282px; top: 34px; color: var(--grey); }
  .doctor + .doctor { margin-top: 8px; }
  .doctor-name { color: var(--purple); font-weight: 700; font-size: 14px; letter-spacing: .2px; line-height: 1.35; }
  .doctor-title { font-size: 11.5px; line-height: 1.4; }
  .contact-list { list-style: none; margin-top: 10px; font-size: 11px; line-height: 1.65; }
  .contact-list li, .office-phone { display: flex; align-items: center; gap: 6px; }
  .icon { width: 10px; height: 10px; fill: var(--purple); flex: none; }
  .offices {
    position: absolute; left: 42px; right: 40px; bottom: 32px;
    display: flex; gap: 70px;
    font-size: 11.5px; line-height: 1.55; color: var(--grey); letter-spacing: .3px;
  }
  .office-label { color: var(--purple); font-weight: 600; font-size: 10px; letter-spacing: 1.5px; }
</style>
</head>
<body>
  <section class="card card-back" aria-label="Card back">
    <div class="wordmark">
      <span class="wordmark-dot"></span>
      <span class="wordmark-text">
        <span class="wordmark-name">HALVERCOTT</span>
        <span class="wordmark-sub">ORTHODONTICS</span>
      </span>
    </div>
  </section>

  <section class="card card-front" aria-label="Card front">
    <span class="accent-bar left"></span>
    <span class="accent-bar right"></span>

    <div class="wordmark">
      <span class="wordmark-dot"></span>
      <span class="wordmark-text">
        <span class="wordmark-name">HALVERCOTT</span>
        <span class="wordmark-sub">ORTHODONTICS</span>
      </span>
    </div>

    <span class="divider"></span>

    <div class="contact">
      <div class="doctor">
        <p class="doctor-name">MARGUERITE L. HALVERCOTT, DMD</p>
        <p class="doctor-title">Managing Director</p>
      </div>
      <div class="doctor">
        <p class="doctor-name">DOUGLAS R. HALVERCOTT, DMD</p>
      </div>
      <ul class="contact-list">
        <li>
          <svg class="icon" viewBox="0 0 24 24" aria-hidden="true"><path d="M2 5h20v14H2z"/><path d="M2 5l10 8 10-8" fill="none" stroke="#fff" stroke-width="2"/></svg>
          frontdesk@halvercottortho.example
        </li>
        <li>
          <svg class="icon" viewBox="0 0 24 24" aria-hidden="true"><circle cx="12" cy="12" r="10"/></svg>
          www.halvercottortho.example
        </li>
      </ul>
    </div>

    <div class="offices">
      <address class="office" style="font-style:normal">
        <p class="office-label">NORTH ANDOVER</p>
        <p>312 Bramblewood Street</p>
        <p>North Andover, MA 01899</p>
        <p class="office-phone">
          <svg class="icon" viewBox="0 0 24 24" aria-hidden="true"><path d="M6.6 10.8a15.1 15.1 0 0 0 6.6 6.6l2.2-2.2c.3-.3.7-.4 1-.2 1.1.4 2.3.6 3.6.6.6 0 1 .4 1 1V20c0 .6-.4 1-1 1A17 17 0 0 1 3 4c0-.6.4-1 1-1h3.5c.6 0 1 .4 1 1 0 1.3.2 2.5.6 3.6.1.3 0 .7-.2 1z"/></svg>
          978.555.0142
        </p>
      </address>
      <address class="office" style="font-style:normal">
        <p class="office-label">METHUEN</p>
        <p>847C Quarry Hollow Street</p>
        <p>Methuen, MA 01898</p>
        <p class="office-phone">
          <svg class="icon" viewBox="0 0 24 24" aria-hidden="true"><path d="M6.6 10.8a15.1 15.1 0 0 0 6.6 6.6l2.2-2.2c.3-.3.7-.4 1-.2 1.1.4 2.3.6 3.6.6.6 0 1 .4 1 1V20c0 .6-.4 1-1 1A17 17 0 0 1 3 4c0-.6.4-1 1-1h3.5c.6 0 1 .4 1 1 0 1.3.2 2.5.6 3.6.1.3 0 .7-.2 1z"/></svg>
          978.555.0187
        </p>
      </address>
    </div>
  </section>
</body>
</html>
```